International Honeymoon Tour Operator needs Business Card

We need to design a business card including our new logo for a new tour operator called Marisol Thorne Getaways. We would like to also include the text 'Personal Tailor-Made Honeymoons for our Guests at a Lower Cost'. Please Include the following details as well; 'Website: www.marisolthornegetaways.co.uk'; 'E-mail: felix@marisolthornegetaways.co.uk'; 'Mobile: 07914263058'. We would like the design to be compatible with the logo and text. The final design should communicate professionalism, modern and ethical.

We want to business card to be double sided.

We would like to be able to easily adjust the e-mail address and contact number in the future for other employees either through you or ourselves.

Target Market(s)

Brides and grooms aged 18-35 predominantly.

Industry/Entity Type

Business

Colors

Designer to choose colors to be used in the design.

Requirements
Must have
• Logo
Requested Text
Double sided
Nice to have
• Additional colour
The wow factor
Should not have
• Images of currency

```html
<!DOCTYPE html>
<html lang="en">
<head>
<meta charset="utf-8">
<title>Marisol Thorne Getaways – Business Card</title>
<link rel="stylesheet" href="https://fonts.googleapis.com/css2?family=Cinzel:wght@700&family=Oswald:wght@600&family=Open+Sans:wght@400&display=swap">
<style>
  :root {
    --leaf-green: #2bd11a;
    --brand-green: #1f8a4c;
    --call-green: #1e9a12;
    --logo-green: #3aa655;
    --logo-light: #b8f06a;
    --paper: #ffffff;
    --ink: #0d0d0d;
  }
  * { box-sizing: border-box; margin: 0; padding: 0; }
  html, body {
    width: 1200px; height: 791px; overflow: hidden;
    background: var(--paper);
  }
  .card {
    position: relative; width: 1200px; height: 791px;
    background: var(--paper);
  }
  .card-frame {
    position: absolute; left: 35px; top: 86px; width: 1128px; height: 617px;
    border: 7px solid var(--leaf-green);
    overflow: hidden;
  }
  .stripe-backdrop {
    position: absolute; inset: 0;
    background: linear-gradient(100deg, #e3fad8 0%, #ffffff 45%, #ffffff 70%, #e6fbdc 100%);
  }
  .tagline {
    position: absolute; left: 0; right: 0; top: 34px;
    text-align: center;
    font-family: "Cinzel", serif; font-weight: 700; font-size: 30px;
    color: var(--ink); white-space: nowrap;
  }
  .logo-art {
    position: absolute; left: 27px; top: 68px; width: 536px; height: 208px;
    border-radius: 40px;
    background: radial-gradient(ellipse at 50% 45%, rgba(58,166,85,0.35) 0%, rgba(184,240,106,0.25) 50%, rgba(255,255,255,0) 75%);
  }
  .brand-name {
    position: absolute; left: 12px; top: 292px; width: 580px;
    font-family: "Open Sans", sans-serif; font-weight: 400;
    color: var(--brand-green); white-space: nowrap;
  }
  .brand-name .brand-main { display: block; font-size: 70px; line-height: 1.05; letter-spacing: -1px; }
  .brand-name .brand-sub { display: block; font-size: 34px; line-height: 1.4; letter-spacing: 10px; padding-left: 10px; }
  .bullet {
    position: absolute; border-radius: 50%;
    background: radial-gradient(circle at 35% 35%, #555 0%, #000 60%);
  }
  .call-line {
    position: absolute; left: 0; top: 0; width: 1114px; height: 603px;
    overflow: visible;
  }
  .call-line text {
    font-family: "Oswald", sans-serif; font-weight: 600;
    fill: var(--call-green);
  }
  .contact-line {
    position: absolute;
    font-family: "Open Sans", sans-serif; font-weight: 400;
    font-size: 30px; color: var(--ink); white-space: nowrap;
  }
  .rule {
    position: absolute; height: 3px; background: var(--leaf-green);
  }
</style>
</head>
<body>
  <main class="card">
    <section class="card-frame">
      <div class="stripe-backdrop" role="img" aria-label="Light green vertical stripe pattern with soft leafy swirls at the edges"></div>

      <h1 class="tagline">Personal Tailor-Made Honeymoons For Guests At A Lower Cost</h1>

      <div class="logo-art" role="img" aria-label="Brand illustration area: two green birds on a dark branch"></div>

      <p class="brand-name"><span class="brand-main">Marisol Thorne</span><span class="brand-sub">GETAWAYS</span></p>

      <span class="bullet" style="left:532px; top:256px; width:16px; height:16px;"></span>
      <svg class="call-line" viewBox="0 0 1114 603" aria-label="Call Us Today: 07914263058">
        <text x="548" y="293" font-size="108" textLength="530" lengthAdjust="spacingAndGlyphs">Call Us Today: 07914263058</text>
      </svg>

      <span class="bullet" style="left:300px; top:510px; width:13px; height:15px;"></span>
      <p class="contact-line" style="left:320px; top:494px;">Website: www.marisolthornegetaways.co.uk</p>

      <span class="rule" style="left:160px; top:533px; width:907px;"></span>
      <span class="rule" style="left:160px; top:542px; width:859px;"></span>

      <span class="bullet" style="left:172px; top:574px; width:12px; height:15px;"></span>
      <p class="contact-line" style="left:192px; top:558px;">Email : felix@marisolthornegetaways.co.uk</p>
    </section>
  </main>
</body>
</html>
```